Travel, Resort and Tourism Advisor

I am looking for a classy and slick website for a travel, resort and tourism website which will offer first hand advise to tourist and fun seekers on the best locations and remarkable places to relax and unwind. We are primary located in the United States but will offer services to people worldwide. My website will feature images and locations and analysis of the best resorts in the Industry. Designers can take an idea from http://wanderquill.example It will include prices, safety tips, culture and how to make the best of your tourism. The website will compare different destinations and recommend places based on the user budget, culture, and ethnic nationality. I would want a colorful and attention seeking website. Have questions ask.

```html
<!DOCTYPE html>
<html lang="en">
<head>
<meta charset="utf-8">
<title>Corvina Advisors — Travel &amp; Tourism</title>
<link href="https://fonts.googleapis.com/css2?family=Montserrat:wght@400;600;700&family=Raleway:wght@300;400;500;600&display=swap" rel="stylesheet">
<style>
:root{
  --teal:#1a86ad;
  --teal-dark:#177a9e;
  --accent:#1a8cb3;
  --ink:#1d1d1f;
  --text:#6f6f6f;
  --light:#9a9a9a;
  --red:#e8503f;
  --cyan:#2ec4dc;
  --green:#4cd261;
  --purple:#c466e0;
  --white:#ffffff;
}
*{box-sizing:border-box;margin:0;padding:0}
html,body{width:1200px;height:3209px;overflow:hidden}
body{font-family:"Raleway",sans-serif;color:var(--text);background:var(--white);position:relative}
.wrap{position:absolute;left:100px;right:100px}

/* top bar */
.topbar{position:absolute;top:0;left:0;width:1200px;height:41px;background:var(--teal);color:#e6f4f9;font-size:12px}
.topbar .contact{position:absolute;left:100px;top:13px;display:flex;gap:34px}
.topbar .contact span{display:flex;align-items:center;gap:8px}
.topbar .social{position:absolute;right:100px;top:15px;display:flex;gap:9px}
.topbar .social i{width:10px;height:10px;border-radius:50%;background:#e6f4f9;display:block}

/* header */
.header{position:absolute;top:41px;left:0;width:1200px;height:113px;background:var(--white)}
.brand{position:absolute;left:100px;top:34px;display:flex;align-items:center;gap:12px}
.brand .dot{width:36px;height:36px;border-radius:50%;background:var(--teal)}
.brand .name{font-family:"Raleway",sans-serif;font-weight:500;font-size:28px;color:var(--teal)}
.nav{position:absolute;right:100px;top:0;height:113px;display:flex;gap:40px;align-items:center;font-family:"Montserrat",sans-serif;font-size:13px;font-weight:600;color:var(--ink)}
.nav .active{color:var(--teal);position:relative;height:113px;display:flex;align-items:center}
.nav .active::after{content:"";position:absolute;left:-8px;right:-8px;bottom:0;height:3px;background:var(--teal)}

/* hero */
.hero{position:absolute;top:154px;left:0;width:1200px;height:590px;background:linear-gradient(180deg,#1f6fc6 0%,#3b92d8 40%,#56b5d8 62%,#bcd3d6 80%,#d9d6cc 100%)}
.hero h1{position:absolute;left:100px;top:214px;color:#fff;font-family:"Montserrat",sans-serif}
.hero h1 small{display:block;font-weight:400;font-size:35px;letter-spacing:1px}
.hero h1 strong{display:block;font-weight:700;font-size:46px;margin-top:6px;letter-spacing:.5px}
.hero .arrow{position:absolute;top:264px}
.search{position:absolute;left:100px;top:528px;width:1000px;height:41px;display:flex;gap:22px}
.search .field{background:#fff;height:41px;display:flex;align-items:center;padding:0 14px;font-size:14px;color:#444}
.search .field em{font-style:normal;color:#b5b5b5;margin-left:14px}
.search .find{width:390px}
.search .dest{width:410px}
.search .go{flex:1;background:var(--cyan);color:#fff;font-family:"Montserrat",sans-serif;font-weight:600;font-size:14px;display:flex;align-items:center;justify-content:center;margin-left:6px}

/* welcome */
.welcome{position:absolute;top:744px;left:0;width:1200px;height:601px}
.sec-title{font-family:"Montserrat",sans-serif;font-weight:700;font-size:30px;color:var(--ink);text-align:center;letter-spacing:.5px}
.sec-title span{color:var(--accent)}
.welcome .sec-title{position:absolute;top:45px;width:100%}
.welcome .intro{position:absolute;top:101px;left:130px;width:940px;text-align:center;font-size:13.5px;line-height:24px;color:#7a7a7a}
.welcome .rule{position:absolute;top:196px;left:340px;width:520px;height:1px;background:#e4e4e4}
.services{position:absolute;top:232px;left:100px;width:1000px;display:flex;justify-content:space-between}
.service{width:240px;text-align:center}
.service .badge{width:128px;height:128px;border-radius:50%;margin:0 auto;border:6px solid #eee;display:flex;align-items:center;justify-content:center}
.service .badge svg{width:56px;height:56px}
.service h3{font-family:"Montserrat",sans-serif;font-weight:700;font-size:15px;color:var(--ink);margin-top:19px}
.service p{font-size:13.5px;line-height:20px;margin:14px auto 0;width:210px}
.service .btn{display:inline-block;margin-top:26px;width:154px;height:45px;line-height:43px;border:2px solid;font-family:"Montserrat",sans-serif;font-size:14px}
.red{color:var(--red)}.cyan{color:var(--cyan)}.green{color:var(--green)}.purple{color:var(--purple)}

/* band */
.band{position:absolute;top:1345px;left:0;width:1200px;height:430px;background:linear-gradient(180deg,#2d98c2 0%,#2a90bb 55%,#3b9ec4 100%);text-align:center;color:#fff}
.band h2{position:absolute;top:55px;width:100%;font-family:"Raleway",sans-serif;font-weight:400;font-size:52px;letter-spacing:.5px}
.band p{position:absolute;top:136px;left:180px;width:840px;font-size:22px;line-height:34px;color:#e4f3f9;letter-spacing:.3px}
.band .book{position:absolute;top:306px;left:465px;width:270px;height:51px;border:2px solid rgba(255,255,255,.7);line-height:47px;font-family:"Montserrat",sans-serif;font-weight:600;font-size:17px;letter-spacing:1px}

/* destinations */
.destinations{position:absolute;top:1775px;left:0;width:1200px;height:574px}
.destinations .sec-title{position:absolute;top:45px;width:100%}
.pager{position:absolute;right:100px;top:52px;display:flex;gap:6px}
.pager i{width:26px;height:26px;border-radius:50%;background:#e6e6e6;display:flex;align-items:center;justify-content:center}
.dest-cards{position:absolute;top:124px;left:100px;width:1000px;display:flex;justify-content:space-between}
.dest{width:316px}
.dest .photo{height:182px}
.dest h3{font-family:"Montserrat",sans-serif;font-weight:400;font-size:20px;color:var(--ink);margin-top:28px;letter-spacing:.5px}
.dest p{font-size:13.5px;line-height:21px;margin-top:8px;color:#8a8a8a}
.dest .more{display:inline-flex;align-items:center;gap:8px;margin-top:38px;height:41px;padding:0 18px;color:#fff;font-size:14px}
.bg-red{background:var(--red)}.bg-cyan{background:var(--cyan)}.bg-green{background:var(--green)}

/* packages */
.packages{position:absolute;top:2349px;left:0;width:1200px;height:543px;background:linear-gradient(180deg,#3a8fbf 0%,#5aa9cc 45%,#7fc0d2 75%,#4ea2c6 100%)}
.packages .sec-title{position:absolute;top:46px;width:100%;color:#fff}
.pkg-cards{position:absolute;top:126px;left:100px;width:1000px;display:flex;justify-content:space-between}
.pkg{width:316px;height:348px;background:#fff}
.pkg .photo{height:184px}
.pkg p{font-size:13px;line-height:21px;text-align:center;padding:14px 22px 0;color:#777}
.pkg .price{display:flex;justify-content:space-between;align-items:flex-end;padding:0 18px;margin-top:18px;border-top:1px solid #eee;padding-top:12px}
.pkg .price small{display:block;font-size:9px;color:#999;letter-spacing:1px}
.pkg .price b{font-family:"Montserrat",sans-serif;font-size:20px;color:var(--ink);font-weight:600}
.pkg .price a{height:32px;line-height:32px;padding:0 14px;color:#fff;font-size:12px;font-family:"Montserrat",sans-serif}

/* footer */
.footer{position:absolute;top:2892px;left:0;width:1200px;height:317px;background:var(--teal);color:#e7f4f9}
.fcol{position:absolute;top:40px}
.fcol h4{font-family:"Montserrat",sans-serif;font-weight:700;font-size:16px;letter-spacing:1px;color:#fff;margin-bottom:18px}
.fcol li{list-style:none;font-size:14px;line-height:30px;display:flex;align-items:center;gap:10px}
.fsep{position:absolute;top:42px;width:1px;height:195px;background:rgba(255,255,255,.2)}
.fsocial{display:flex;gap:8px;margin-top:18px}
.fsocial i{width:38px;height:38px;border-radius:50%;border:2px solid #fff;display:block}
.footer .rule{position:absolute;top:244px;left:100px;width:1000px;height:1px;background:rgba(255,255,255,.35)}
.footer .copy{position:absolute;top:270px;left:100px;font-size:12px}
.footer .code{position:absolute;top:268px;right:100px;font-size:13px}
</style>
</head>
<body>

<div class="topbar">
  <div class="contact">
    <span><svg width="12" height="12" viewBox="0 0 24 24"><path fill="#e6f4f9" d="M6.6 10.8a15 15 0 0 0 6.6 6.6l2.2-2.2c.3-.3.7-.4 1-.2 1.1.4 2.3.6 3.6.6.6 0 1 .4 1 1V20c0 .6-.4 1-1 1A17 17 0 0 1 3 4c0-.6.4-1 1-1h3.5c.6 0 1 .4 1 1 0 1.3.2 2.5.6 3.6.1.3 0 .7-.2 1z"/></svg>Call us: &nbsp;(555) 014-2290</span>
    <span><svg width="13" height="10" viewBox="0 0 26 20"><rect x="1" y="1" width="24" height="18" fill="none" stroke="#e6f4f9" stroke-width="2"/><path d="M1 1l12 10L25 1" fill="none" stroke="#e6f4f9" stroke-width="2"/></svg>Email us: hello@corvinatrips.example</span>
  </div>
  <div class="social"><i></i><i></i><i></i><i></i><i></i></div>
</div>

<header class="header">
  <div class="brand"><span class="dot"></span><span class="name">Corvina Advisors</span></div>
  <nav class="nav">
    <span class="active">HOME</span><span>HOTELS</span><span>PAGES</span><span>PLACES</span><span>GALLERY</span><span>BLOG</span><span>CONTACT US</span>
  </nav>
</header>

<section class="hero" role="img" aria-label="Tropical beach with a palm tree and two deck chairs facing a blue sea">
  <h1><small>WE ARE A</small><strong>TRAVEL &amp; TOURISM ADVISOR.</strong></h1>
  <svg class="arrow" style="left:24px" width="24" height="40" viewBox="0 0 24 40"><path d="M18 6L6 20l12 14" fill="none" stroke="rgba(255,255,255,.7)" stroke-width="3"/></svg>
  <svg class="arrow" style="right:24px" width="24" height="40" viewBox="0 0 24 40"><path d="M6 6l12 14L6 34" fill="none" stroke="rgba(255,255,255,.7)" stroke-width="3"/></svg>
  <div class="search">
    <div class="field find">Find: <em>Hotels, Restaurants, Things to Do</em></div>
    <div class="field dest">Destination: <em>Worldwide</em></div>
    <div class="go">SEARCH</div>
  </div>
</section>

<section class="welcome">
  <h2 class="sec-title">WELCOME TO <span>CORVINA ADVISORS</span></h2>
  <p class="intro">Sed ut perspiciatis unde omnis iste natus error sit voluptatem accusantium doloremque laudantium, totam rem aperiam, eaque ipsa quae ab illo inventore veritatis et quasi architecto beatae vitae dicta sunt explicabo. Nemo enim ipsam voluptatem quia voluptas sit aspernatur aut odit aut fugit, sed quia consequuntur magni dolores eos qui ratione voluptatem sequi nesciunt.</p>
  <div class="rule"></div>
  <div class="services">
    <div class="service">
      <div class="badge" style="background:var(--red)"><svg viewBox="0 0 56 56"><path d="M28 48S6 34 6 19a11 11 0 0 1 22-3 11 11 0 0 1 22 3c0 15-22 29-22 29z" fill="#fff"/><path d="M18 30l16-8 4 2-8 5 3 6-2 1-4-5-5 2z" fill="var(--red)"/></svg></div>
      <h3>FLIGHTS</h3>
      <p>Praesent vestibulum aenean nonummy endrerit mauris. Cum sociis natoque..</p>
      <span class="btn red">READ MORE</span>
    </div>
    <div class="service">
      <div class="badge" style="background:var(--cyan)"><svg viewBox="0 0 56 56"><path d="M6 14v30M6 36h44v8M6 30h44" fill="none" stroke="#fff" stroke-width="3"/><rect x="9" y="22" width="10" height="7" rx="3" fill="#fff"/><rect x="22" y="22" width="28" height="7" fill="#fff"/></svg></div>
      <h3>HOTELS</h3>
      <p>Praesent vestibulum aenean nonummy endrerit mauris. Cum sociis natoque..</p>
      <span class="btn cyan">READ MORE</span>
    </div>
    <div class="service">
      <div class="badge" style="background:var(--green)"><svg viewBox="0 0 56 56"><path d="M14 26l4-10h20l4 10" fill="none" stroke="#fff" stroke-width="3"/><rect x="9" y="26" width="38" height="12" rx="3" fill="#fff"/><rect x="12" y="37" width="7" height="7" fill="#fff"/><rect x="37" y="37" width="7" height="7" fill="#fff"/><circle cx="16" cy="32" r="2.5" fill="var(--green)"/><circle cx="40" cy="32" r="2.5" fill="var(--green)"/></svg></div>
      <h3>CARS</h3>
      <p>Praesent vestibulum aenean nonummy endrerit mauris. Cum sociis natoque..</p>
      <span class="btn green">READ MORE</span>
    </div>
    <div class="service">
      <div class="badge" style="background:var(--purple)"><svg viewBox="0 0 56 56"><circle cx="24" cy="12" r="5" fill="#fff"/><path d="M17 20h14v14h-3v14h-8V34h-3z" fill="#fff"/><path d="M34 18a7 4 0 0 1 14 0z" fill="#fff"/><path d="M33 19h16" stroke="#fff" stroke-width="2"/></svg></div>
      <h3>RESTAURANTS</h3>
      <p>Praesent vestibulum aenean nonummy endrerit mauris. Cum sociis natoque..</p>
      <span class="btn purple">READ MORE</span>
    </div>
  </div>
</section>

<section class="band" role="img" aria-label="Blue-tinted backdrop of world landmarks and a palm tree">
  <h2>We are a Travel &amp; Tourism advisor</h2>
  <p>Donec sodales sagittis magna. Sed consequat, leo eget bibendum sodales. There are many variations of passages of Lorem Ipsum available, but the majority have suffered alteration in some form, by injected humour, or randomised words which don't look even slightly believable.</p>
  <div class="book">BOOK NOW !</div>
</section>

<section class="destinations">
  <h2 class="sec-title">TOP <span>DESTINATIONS</span></h2>
  <div class="pager">
    <i><svg width="8" height="10" viewBox="0 0 8 10"><path d="M6 1L2 5l4 4" fill="none" stroke="#666" stroke-width="1.6"/></svg></i>
    <i><svg width="8" height="10" viewBox="0 0 8 10"><path d="M2 1l4 4-4 4" fill="none" stroke="#666" stroke-width="1.6"/></svg></i>
  </div>
  <div class="dest-cards">
    <article class="dest">
      <div class="photo" role="img" aria-label="Hiker on a snowy mountain ridge under a bright sky" style="background:linear-gradient(180deg,#3d6fb8 0%,#8cb6e0 45%,#dfe7ef 75%,#5c6d80 100%)"></div>
      <h3>CLARITAS EST ETIAM</h3>
      <p>The simplicity and value of a destination wedding in a beautiful setting is appealing to many couples..</p>
      <span class="more bg-red">Read More <svg width="6" height="9" viewBox="0 0 6 9"><path d="M1 1l3.5 3.5L1 8" fill="none" stroke="#fff" stroke-width="1.4"/></svg></span>
    </article>
    <article class="dest">
      <div class="photo" role="img" aria-label="Family walking on a boat deck beside turquoise water" style="background:linear-gradient(180deg,#9fd4ea 0%,#4fb3d6 45%,#2e9ec6 65%,#b7835f 100%)"></div>
      <h3>EODEM MODO</h3>
      <p>Your honeymoon should be relaxing, fun, romantic and memorable. We will assist and guide you in finding..</p>
      <span class="more bg-cyan">Read More <svg width="6" height="9" viewBox="0 0 6 9"><path d="M1 1l3.5 3.5L1 8" fill="none" stroke="#fff" stroke-width="1.4"/></svg></span>
    </article>
    <article class="dest">
      <div class="photo" role="img" aria-label="Two riders on a yellow inflatable tube across the sea" style="background:linear-gradient(180deg,#2f7fb0 0%,#2b8fc0 50%,#e0c54a 70%,#2d85b5 100%)"></div>
      <h3>UT WISI ENIM</h3>
      <p>Family, friends, couples or whomever you care to getaway with; our team are experts in a multitude of destinations..</p>
      <span class="more bg-green">Read More <svg width="6" height="9" viewBox="0 0 6 9"><path d="M1 1l3.5 3.5L1 8" fill="none" stroke="#fff" stroke-width="1.4"/></svg></span>
    </article>
  </div>
</section>

<section class="packages" role="img" aria-label="Tropical coast with green hills and calm lagoon water">
  <h2 class="sec-title">TOP TOUR PACKAGES</h2>
  <div class="pkg-cards">
    <article class="pkg">
      <div class="photo" role="img" aria-label="Park with a monument and green lawns" style="background:linear-gradient(180deg,#6fa8dc 0%,#b9d6ee 45%,#6aa04a 70%,#4f8a36 100%)"></div>
      <p>Nunc commodo ipsum in diam pulvinar, laoreet tempor tellus molestie. Maecenas blandit sem turpis, nec luctus nunc...</p>
      <div class="price"><div><small>STARTS FROM</small><b>$250</b></div><a class="bg-red">VIEW DETAILS</a></div>
    </article>
    <article class="pkg">
      <div class="photo" role="img" aria-label="Snowy mountains reflected in a glacial bay" style="background:linear-gradient(180deg,#1f5fa8 0%,#5c9bd6 35%,#e8f0f6 55%,#2b6ea8 100%)"></div>
      <p>Nunc commodo ipsum in diam pulvinar, laoreet tempor tellus molestie. Maecenas blandit sem turpis, nec luctus nunc...</p>
      <div class="price"><div><small>STARTS FROM</small><b>$120</b></div><a class="bg-cyan">VIEW DETAILS</a></div>
    </article>
    <article class="pkg">
      <div class="photo" role="img" aria-label="Cliffs above a deep blue sea" style="background:linear-gradient(180deg,#3a78c0 0%,#8fb8de 40%,#c9bfa5 58%,#1f5d9a 100%)"></div>
      <p>Nunc commodo ipsum in diam pulvinar, laoreet tempor tellus molestie. Maecenas blandit sem turpis, nec luctus nunc...</p>
      <div class="price"><div><small>STARTS FROM</small><b>$150</b></div><a class="bg-green">VIEW DETAILS</a></div>
    </article>
  </div>
</section>

<footer class="footer">
  <div class="fcol" style="left:100px"><h4>COMPANY</h4><ul><li>Home</li><li>About Us</li><li>Blog</li><li>News</li><li>Travels</li></ul></div>
  <div class="fsep" style="left:233px"></div>
  <div class="fcol" style="left:276px"><h4>SERVICES</h4><ul><li>Flights</li><li>Hotels</li><li>Cars</li><li>Restaurants</li><li>Others</li></ul></div>
  <div class="fsep" style="left:456px"></div>
  <div class="fcol" style="left:498px"><h4>GET IN TOUCH</h4><ul>
    <li><svg width="13" height="13" viewBox="0 0 24 24"><path fill="#e7f4f9" d="M6.6 10.8a15 15 0 0 0 6.6 6.6l2.2-2.2c.3-.3.7-.4 1-.2 1.1.4 2.3.6 3.6.6.6 0 1 .4 1 1V20c0 .6-.4 1-1 1A17 17 0 0 1 3 4c0-.6.4-1 1-1h3.5c.6 0 1 .4 1 1 0 1.3.2 2.5.6 3.6.1.3 0 .7-.2 1z"/></svg>Call us on (01) 55501234</li>
    <li><svg width="13" height="10" viewBox="0 0 26 20"><rect x="1" y="1" width="24" height="18" fill="none" stroke="#e7f4f9" stroke-width="2"/><path d="M1 1l12 10L25 1" fill="none" stroke="#e7f4f9" stroke-width="2"/></svg>info@corvinatrips.example</li></ul></div>
  <div class="fsep" style="left:725px"></div>
  <div class="fcol" style="left:768px"><h4>WHY US</h4><ul><li>Customers</li><li>Team</li><li>FAQ</li><li>Contact</li></ul></div>
  <div class="fsep" style="left:885px"></div>
  <div class="fcol" style="left:926px"><h4>FOLLLOW US</h4><ul><li>Please connect with us on</li></ul><div class="fsocial"><i></i><i></i><i></i><i></i></div></div>
  <div class="rule"></div>
  <div class="copy">© 2016 Company Name &nbsp;All right reserved &nbsp;Term of Use</div>
  <div class="code">C16</div>
</footer>

</body>
</html>
```